Open House 2017

We need a flyer for an insert for a newspaper for an open house that we are going to have and we are also wanting to list the front of the flyer the 3 pictures of our real estate agents and our Logo.

For the real estate agents : The one with Purple shirt would be the middle picture.

Attached also is our current Logo, Please re-design our Logo a bit to make it look better.

Target Market(s)

Residential and commercial and Land In our rural areas.

Industry/Entity Type

House

Requirements
Must have
• Front page -
• Our logo at the top our 3 pictures at the top after our logo and business address.
• Middle of page Some thing worded similar to the following:"let us place a SOLD sign in your front yard". Or
• " Sold vs. For Sale which would you like to see in your front yard?"
• Our colors for our agency are Gold and Black (the whole flyer does not need to be this color though)
• Join us for an open house in our office
• Wednesday March 1
• 3-6pm
• Back page of flyer: "If you would like to add your name to the Sold Properties list, give us a call today!
• Sold listings which we will get sent to you will also be listed on the back page.
Should not have
• do not make the flyer too "busy" with too many pictures and wording.

```html
<!DOCTYPE html>
<html lang="en">
<head>
<meta charset="utf-8">
<title>Marlowe Realty – Open House Flyer</title>
<link rel="stylesheet" href="https://fonts.googleapis.com/css2?family=Cinzel:wght@400;600;700&family=Libre+Caslon+Text:ital,wght@0,700;1,400&display=swap">
<style>
  :root {
    --canvas: #f2f2f2;
    --black: #0a0a0a;
    --gold: #e2ae3f;
    --gold-deep: #c9922a;
    --gold-light: #f7d98e;
    --gold-pale: #fbe7b2;
    --ink: #111111;
    --photo-a: #9a9a9a;
    --photo-b: #6e6e6e;
  }
  * { margin: 0; padding: 0; box-sizing: border-box; }
  html, body { width: 1200px; height: 861px; overflow: hidden; background: var(--canvas); }
  .flyer {
    position: absolute; left: 300px; top: 16px;
    width: 600px; height: 830px;
    background: radial-gradient(ellipse at 55% 45%, var(--gold-pale) 0%, var(--gold-light) 35%, var(--gold) 75%, var(--gold-deep) 100%);
    overflow: hidden;
    font-family: "Cinzel", "Times New Roman", serif;
    color: var(--ink);
    text-align: center;
    box-shadow: 0 6px 24px rgba(0,0,0,.18);
  }
  .flyer__swoosh { position: absolute; inset: 0; }
  .masthead {
    position: absolute; left: 0; top: 0; width: 100%; height: 128px;
    background: var(--black);
    padding-top: 18px;
  }
  .brand-name {
    font-family: "Libre Caslon Text", "Times New Roman", serif;
    font-weight: 700; font-size: 44px; letter-spacing: .5px;
    color: var(--gold); line-height: 1;
  }
  .brand-tagline {
    font-family: "Libre Caslon Text", "Times New Roman", serif;
    font-style: italic; font-weight: 400; font-size: 18px; color: var(--gold);
    margin-top: 8px; line-height: 1.2;
  }
  .brand-address {
    font-family: "Cinzel", "Times New Roman", serif;
    font-weight: 600; font-size: 13px; letter-spacing: 1px; color: var(--gold);
    margin-top: 7px; line-height: 1.2;
  }
  .agents {
    position: absolute; top: 178px; left: 0; width: 100%;
    display: flex; justify-content: center; gap: 18px;
  }
  .agent-photo {
    width: 152px; height: 160px; border-radius: 50%;
    background: radial-gradient(circle at 50% 40%, var(--photo-a), var(--photo-b));
    border: 5px solid var(--gold-deep);
    box-shadow: 0 3px 8px rgba(0,0,0,.25);
  }
  .headline {
    position: absolute; top: 372px; width: 100%;
    font-weight: 600; font-size: 33px; line-height: 46px;
  }
  .invite { position: absolute; top: 500px; width: 100%; }
  .invite__lead, .invite__place { font-weight: 600; font-size: 23px; line-height: 1; }
  .invite__title { font-weight: 700; font-size: 48px; line-height: 1; margin: 12px 0 10px; }
  .event-date {
    position: absolute; top: 666px; width: 100%;
    font-weight: 600; font-size: 31px;
  }
  .footer-band {
    position: absolute; left: 0; bottom: 0; width: 100%; height: 88px;
    background: var(--black);
    display: flex; align-items: center; justify-content: center;
  }
  .copyright {
    font-family: "Libre Caslon Text", "Times New Roman", serif;
    font-style: italic; font-weight: 400; font-size: 19px; color: var(--gold);
  }
</style>
</head>
<body>
  <main class="flyer">
    <svg class="flyer__swoosh" width="600" height="830" viewBox="0 0 600 830" aria-hidden="true">
      <path d="M0 560 C 120 600, 200 700, 300 742 L 0 742 Z" fill="#d9a23a" opacity=".45"/>
      <path d="M0 600 C 90 640, 170 700, 230 742 L 0 742 Z" fill="#c98f28" opacity=".35"/>
      <path d="M70 128 C 40 300, 110 520, 300 742" fill="none" stroke="#fff2c8" stroke-width="2" opacity=".5"/>
    </svg>

    <header class="masthead">
      <div class="brand-name">Marlowe Realty LLC</div>
      <div class="brand-tagline">“Where the phone is ALWAYS on.”</div>
      <div class="brand-address">214 Harvest Lane · Cedar Plains, MN 56000</div>
    </header>

    <section class="agents">
      <div class="agent-photo" role="img" aria-label="Portrait photo of agent, woman in white shirt"></div>
      <div class="agent-photo" role="img" aria-label="Portrait photo of agent, man in purple shirt"></div>
      <div class="agent-photo" role="img" aria-label="Portrait photo of agent, man in dark checked shirt"></div>
    </section>

    <h1 class="headline">Let us place a sold sign<br>in your front yard</h1>

    <section class="invite">
      <p class="invite__lead">Join us for an</p>
      <p class="invite__title">Open House</p>
      <p class="invite__place">In our office</p>
    </section>

    <p class="event-date">Wednesday March 1 (3-6 pm)</p>

    <footer class="footer-band">
      <p class="copyright">© Copyright 2016 Marlowe Realty LLC</p>
    </footer>
  </main>
</body>
</html>
```